Business Cards Design for the electrical wholesaler: clean bold dynamic :)

We need a business card design that would follow our latest brand guidelines. As an electrical wholesaler we want to bring a fresh look and feel into the industry. The design should be clean bold and dynamic. It should come alive with the renewed energy of our green colour. Our grey colour should keep things balanced and complement the notion of maturity and responsibility. We employ Lato as a corporate font however are not bound by this font and we’re open to interpretation here.

Target Market(s)

Electrical contractors

Industry/Entity Type

Business

Contact Information for Business Card

Logo
Name & Surname: Olena Dovbush
Job Title: Director of Marketing
Email: helen.dovbush@mailvane.example
Cell phone: XXX.XXX.XXXX
Address: 20917 - 87 Ave. Edmonton, AB, Canada. T6K 2R8
Business Phone: 780.555.0187
Website: www.qorvil.example

Font styles to use
Other font styles liked:
• Lato

Requirements
Must have
• Logo & website
Nice to have
• Brand elements - some of them you may find in the attached Brand Guidelines (e.g. three lines on the background signifying "W")

```html
<!DOCTYPE html>
<html lang="en">
<head>
<meta charset="utf-8">
<title>Qorvil business cards</title>
<link href="https://fonts.googleapis.com/css2?family=Lato:wght@400;700;900&display=swap" rel="stylesheet">
<style>
  :root {
    --brand-green: #6cc400;
    --brand-grey-dark: #3f4040;
    --brand-grey-mid: #5f6161;
    --brand-grey-light: #767878;
    --paper-white: #ffffff;
    --ink-black: #1c1c1c;
    --backdrop: #e9e9e6;
  }
  * { box-sizing: border-box; margin: 0; padding: 0; }
  html, body {
    width: 1200px; height: 800px; overflow: hidden;
    background: var(--backdrop);
    font-family: "Lato", sans-serif;
  }
  .sheet {
    width: 1200px; height: 800px;
    display: flex; align-items: center; justify-content: center; gap: 40px;
  }
  .card {
    position: relative;
    width: 560px; height: 320px;
    border-radius: 4px;
    overflow: hidden;
    box-shadow: 0 6px 18px rgba(0,0,0,.18);
  }

  /* Front */
  .card--front {
    background: var(--brand-green);
    display: flex; align-items: center; justify-content: center;
  }
  .wordmark { color: var(--paper-white); text-align: left; }
  .wordmark__name {
    display: flex; align-items: center; gap: 14px;
    font-weight: 700; font-size: 92px; line-height: .9; letter-spacing: 1px;
  }
  .wordmark__dot {
    width: 30px; height: 30px; border-radius: 50%;
    background: var(--paper-white);
  }
  .wordmark__tagline {
    font-weight: 700; font-size: 17px; letter-spacing: .5px;
    margin-top: 8px; text-transform: uppercase;
  }

  /* Back */
  .card--back {
    background: linear-gradient(135deg, var(--brand-grey-light) 0%, var(--brand-grey-mid) 45%, var(--brand-grey-dark) 100%);
  }
  .texture {
    position: absolute; inset: 0;
    background: radial-gradient(ellipse at 30% 20%, rgba(108,196,0,.18), rgba(108,196,0,0) 60%);
  }
  .card--back .wordmark {
    position: absolute; top: 28px; right: 34px;
  }
  .card--back .wordmark__name { font-size: 64px; justify-content: flex-end; }
  .card--back .wordmark__dot { width: 22px; height: 22px; background: var(--brand-green); }
  .card--back .wordmark__tagline { font-size: 14px; text-align: right; margin-top: 6px; }

  .info-panel {
    position: absolute; left: 22px; right: 14px; top: 152px; bottom: 14px;
    background: var(--brand-green);
    border-radius: 46px 0 40px 0;
    display: flex; align-items: center;
    padding: 0 26px 0 34px;
    color: var(--paper-white);
  }
  .contact-list { list-style: none; font-size: 15px; line-height: 1.45; }
  .contact-list li { display: flex; align-items: flex-start; gap: 8px; }
  .contact-list svg { width: 14px; height: 14px; margin-top: 4px; flex: none; fill: var(--paper-white); }
  .contact-list .address span { display: block; }
  .divider {
    width: 3px; height: 118px; background: var(--paper-white);
    margin: 0 26px 0 22px; flex: none;
  }
  .person__name { color: var(--ink-black); font-weight: 900; font-size: 24px; line-height: 1.1; }
  .person__title { font-weight: 700; font-size: 14px; }
</style>
</head>
<body>
<main class="sheet">
  <section class="card card--front" aria-label="Card front">
    <div class="wordmark">
      <div class="wordmark__name"><span class="wordmark__dot"></span>qorvil</div>
      <div class="wordmark__tagline">Electrical Wholesalers</div>
    </div>
  </section>

  <section class="card card--back" aria-label="Card back">
    <div class="texture" role="img" aria-label="Subtle green honeycomb texture over grey"></div>
    <div class="wordmark">
      <div class="wordmark__name"><span class="wordmark__dot"></span>qorvil</div>
      <div class="wordmark__tagline">Electrical Wholesalers</div>
    </div>

    <div class="info-panel">
      <ul class="contact-list">
        <li><svg viewBox="0 0 16 16"><path d="M1 3h14v10H1z M2 4v.5l6 4 6-4V4z" fill-rule="evenodd"/></svg>helen.dovbush@mailvane.example</li>
        <li><svg viewBox="0 0 16 16"><path d="M4 1h8v14H4z M5 2.5v10h6v-10z M7 13.2h2v1H7z" fill-rule="evenodd"/></svg>XXX.XXX.XXXX</li>
        <li><svg viewBox="0 0 16 16"><path d="M3.5 1.5l3 3-1.5 2c1 2 2.5 3.5 4.5 4.5l2-1.5 3 3-2 2C6 14 2 10 1.5 3.5z"/></svg>780.555.0187</li>
        <li><svg viewBox="0 0 16 16"><path d="M8 1a7 7 0 1 0 0 14A7 7 0 0 0 8 1zm0 1.5c.8 0 1.7 1.6 2 4H6c.3-2.4 1.2-4 2-4zM2.6 7.5h2c0-1.8.4-3.3 1-4.3a5.5 5.5 0 0 0-3 4.3zm8.8 0h2a5.5 5.5 0 0 0-3-4.3c.6 1 1 2.5 1 4.3zM6 8.5h4c-.3 2.4-1.2 4-2 4s-1.7-1.6-2-4zm-3.4 0a5.5 5.5 0 0 0 3 4.3c-.6-1-1-2.5-1-4.3zm8.8 0c0 1.8-.4 3.3-1 4.3a5.5 5.5 0 0 0 3-4.3z"/></svg>www.qorvil.example</li>
        <li class="address"><svg viewBox="0 0 16 16"><path d="M8 1.5L1 8h2v6h4v-4h2v4h4V8h2z"/></svg><div><span>20917 - 87 Ave.</span><span>Edmonton, AB, Canada. T6K 2R8</span></div></li>
      </ul>
      <div class="divider"></div>
      <div class="person">
        <div class="person__name">Olena Dovbush</div>
        <div class="person__title">Director of Marketing</div>
      </div>
    </div>
  </section>
</main>
</body>
</html>
```